Gaming Website - fragvault.co.uk

I have an existing website www.fragvault.co.uk, I'd like to have it redesigned so it has more of a gaming feel to it. Something along the lines of similar websites:

www.lomantix.org
www.vyrndash.com
www.bemkroft.com
www.quidlane.com
www.pv-racking.com
www.hornbeamtactics.com

Target Market(s)

Gamers - First Person Shooter

Requirements
Must have
• Internal page: sidebar, form and a table with data

```html
<!DOCTYPE html>
<html lang="en">
<head>
<meta charset="utf-8">
<title>FragVault — Mixes</title>
<link href="https://fonts.googleapis.com/css2?family=Arimo:wght@400;700&display=swap" rel="stylesheet">
<style>
:root{
  --bg-top:#3a230e;
  --bg-bottom:#050302;
  --brown-dark:#5a2a0c;
  --brown-mid:#6e3410;
  --orange-light:#f7b44f;
  --orange-text:#e8872b;
  --panel-grey:#e9e9e9;
  --row-a:#f4f4f4;
  --row-b:#e9e9e9;
  --live:#1f4fd8;
  --lobby:#ef8a1f;
  --ink:#222;
}
*{box-sizing:border-box;margin:0;padding:0}
html,body{width:1051px;height:1200px;overflow:hidden}
body{font-family:"Arimo",Arial,sans-serif;background:linear-gradient(180deg,var(--bg-top) 0,#24150a 400px,var(--bg-bottom) 1000px);color:var(--ink);position:relative}
.abs{position:absolute}
.top-links{right:150px;top:12px;font-size:10px;color:var(--orange-text)}
.top-links span{margin:0 5px;color:#c0833f}
.header{left:120px;top:34px;width:811px;height:96px;border-radius:12px 12px 0 0;background:linear-gradient(90deg,#6a3512 0,#7c4318 25%,#5d2e0e 55%,#3f1d08 100%)}
.header-art{left:175px;top:0;width:410px;height:96px;background:linear-gradient(90deg,rgba(0,0,0,0),rgba(150,95,45,.45) 40%,rgba(120,70,30,.35) 75%,rgba(0,0,0,0))}
.brand{left:32px;top:28px;display:flex;align-items:center;gap:8px;font-size:26px;font-weight:700;color:#f2f2f2}
.brand i{width:14px;height:14px;background:#f2f2f2;display:block}
.login{right:22px;top:14px;font-size:10px;color:#f0d6b8}
.login .field{display:flex;align-items:center;justify-content:flex-end;margin-bottom:6px}
.login input{width:155px;height:19px;margin-left:8px;border:1px solid #5a2c0c;border-radius:3px;background:#3a1a06}
.login .actions{display:flex;align-items:center;justify-content:flex-end;gap:18px;margin-top:6px}
.btn-login{background:linear-gradient(#f7b044,#d97614);color:#3a1400;font-weight:700;font-size:10px;padding:4px 6px;border-radius:3px}
.login .links{color:var(--orange-text)}
.nav{left:120px;top:130px;width:811px;height:29px;background:linear-gradient(#f7a53f,#dd7a18);display:flex;font-size:10px;font-weight:700;color:#fff}
.nav a{display:flex;align-items:center;justify-content:center;height:100%;border-right:1px solid #c26a18;text-shadow:0 1px 0 #8a4508}
.nav a.active{background:#6a300e}
.band{left:120px;top:159px;width:811px;height:31px;background:var(--brown-mid);border-bottom:1px solid #2a1204}
.title-band{left:120px;top:190px;width:811px;height:60px;background:linear-gradient(#5a2a0c,#4a2208);border:3px solid #6e3410}
.title-band h1{position:absolute;left:17px;top:17px;font-size:15px;font-weight:400;color:#f0d8c0}
.online-box{position:absolute;right:10px;top:13px;width:146px;height:27px;background:#3a1a06;border-radius:3px;color:#f0d8c0;font-size:11px;display:flex;align-items:center;padding-left:22px}
.content{left:120px;top:250px;width:811px;height:866px;background:#fff}
.banner{left:15px;top:16px;width:553px;height:65px;border:2px solid #6e3410;background:linear-gradient(90deg,#7d6a3a,#a07a4c 30%,#8a4a28 60%,#6a2c14)}
.mixes{left:15px;top:83px;width:553px;border-collapse:collapse;font-size:9.5px}
.mixes th{background:var(--brown-dark);color:#fff;font-weight:400;font-size:11px;height:29px;text-align:left;padding-left:12px}
.mixes td{height:29.5px;padding-left:12px}
.mixes tr:nth-child(odd) td{background:var(--row-a)}
.mixes tr:nth-child(even) td{background:var(--row-b)}
.live{color:var(--live);font-weight:700}
.lobby{color:var(--lobby);font-weight:700}
.view{text-decoration:underline}
.sidebar{left:588px;top:16px;width:206px;height:817px;background:var(--panel-grey);border:1px solid #ddd}
.side-title{left:-3px;top:11px;width:200px;height:28px;background:var(--brown-dark);border-radius:0 5px 5px 0;color:#fff;font-size:12px;display:flex;align-items:center;padding-left:11px}
.stat-box{left:13px;width:180px;background:var(--brown-dark);color:#f3e3d0;font-size:10.5px}
.stat-box .head{display:flex;justify-content:space-between;padding:8px 16px;color:var(--orange-light);font-size:12px;border-bottom:1px solid #d9b48a}
.stat-box .rows{padding:8px 16px}
.stat-box .r{display:flex;height:17px}
.more{display:inline-block;margin-top:5px;background:linear-gradient(#f7b044,#d97614);color:#4a1a00;font-weight:700;font-size:10px;padding:4px 9px;border-radius:3px}
.contact{left:13px;top:325px;width:180px;height:285px;padding:20px 18px;font-size:10px;color:#222}
.contact label{display:block;margin-bottom:3px}
.contact input,.contact textarea{display:block;width:100%;height:19px;border:1px solid #bbb;background:#fff;margin-bottom:12px;resize:none}
.contact textarea{height:75px}
.contact .btns{display:flex;justify-content:space-between;margin-top:2px}
.contact .btns span{background:linear-gradient(#8a2a0c,#5a1804);color:#fff;width:57px;height:19px;display:flex;align-items:center;justify-content:center;border-radius:3px}
.ad{left:13px;top:617px;width:180px;height:121px;border:1px solid #555;background:linear-gradient(135deg,#5a0c10,#a02026 50%,#5a0c10)}
.follow{left:0;top:752px;width:204px;height:63px;background:#fff;border-top:1px solid #ddd;padding:9px 12px;font-size:11.5px;font-weight:700;font-style:italic;color:#333}
.follow .icons{display:flex;gap:5px;margin-top:6px}
.follow .icons span{width:27px;height:27px;border-radius:5px;display:block}
.footer-links{left:0;width:1051px;top:1138px;text-align:center;font-size:10px;color:#b9a48e}
.copy{left:0;width:1051px;top:1164px;text-align:center;font-size:10px;color:#7a6a5c}
</style>
</head>
<body>
<div class="abs top-links">Home<span>|</span>Site Map<span>|</span>Career<span>|</span>Contact Us</div>

<div class="abs header">
  <div class="abs header-art" role="img" aria-label="Blended game artwork collage"></div>
  <div class="abs brand"><i></i>FragVault</div>
  <div class="abs login">
    <div class="field">Email:<input></div>
    <div class="field">Password:<input></div>
    <div class="actions"><span class="btn-login">▸▸ Login</span><span class="links">Register | Recover</span></div>
  </div>
</div>

<nav class="abs nav">
  <a class="active" style="width:73px">MIXES</a>
  <a style="width:87px">RANKING</a>
  <a style="width:83px">AWARDS</a>
  <a style="width:78px">FORUM</a>
  <a style="width:85px">REVIEWS</a>
  <a style="width:80px;border:none">MOVIES</a>
</nav>
<div class="abs band"></div>
<div class="abs title-band"><h1>Mixes</h1><div class="online-box">Users online: 352</div></div>

<main class="abs content">
  <div class="abs banner" role="img" aria-label="VectorStrike game banner with soldier artwork"></div>
  <table class="abs mixes">
    <thead><tr><th style="width:125px">Server/Sponsor</th><th style="width:56px">Rel%</th><th style="width:53px">Type</th><th style="width:45px">MR</th><th style="width:55px">Map</th><th style="width:57px">Score</th><th style="width:58px">Users</th><th style="width:54px">Status</th><th></th></tr></thead>
    <tbody>
<tr><td>#01 - VX/TX</td><td>90</td><td>VTX</td><td>15</td><td>vx_dune2</td><td>9-15</td><td>10/10</td><td class="live">LIVE</td><td class="view">View</td></tr>
<tr><td>#01 - VX/TX</td><td>90</td><td>VTX</td><td>15</td><td>vx_dune2</td><td>9-15</td><td>10/10</td><td class="lobby">LOBBY</td><td class="view">View</td></tr>
<tr><td>#01 - VX/TX</td><td>90</td><td>VTX</td><td>15</td><td>vx_dune2</td><td>9-15</td><td>10/10</td><td class="live">LIVE</td><td class="view">View</td></tr>
<tr><td>#01 - VX/TX</td><td>90</td><td>VTX</td><td>15</td><td>vx_dune2</td><td>9-15</td><td>10/10</td><td class="live">LIVE</td><td class="view">View</td></tr>
<tr><td>#01 - VX/TX</td><td>90</td><td>VTX</td><td>15</td><td>vx_dune2</td><td>9-15</td><td>10/10</td><td class="live">LIVE</td><td class="view">View</td></tr>
<tr><td>#01 - VX/TX</td><td>90</td><td>VTX</td><td>15</td><td>vx_dune2</td><td>9-15</td><td>10/10</td><td class="live">LIVE</td><td class="view">View</td></tr>
<tr><td>#01 - VX/TX</td><td>90</td><td>VTX</td><td>15</td><td>vx_dune2</td><td>9-15</td><td>10/10</td><td class="live">LIVE</td><td class="view">View</td></tr>
<tr><td>#01 - VX/TX</td><td>90</td><td>VTX</td><td>15</td><td>vx_dune2</td><td>9-15</td><td>10/10</td><td class="live">LIVE</td><td class="view">View</td></tr>
<tr><td>#01 - VX/TX</td><td>90</td><td>VTX</td><td>15</td><td>vx_dune2</td><td>9-15</td><td>10/10</td><td class="live">LIVE</td><td class="view">View</td></tr>
<tr><td>#01 - VX/TX</td><td>90</td><td>VTX</td><td>15</td><td>vx_dune2</td><td>9-15</td><td>10/10</td><td class="lobby">LOBBY</td><td class="view">View</td></tr>
<tr><td>#01 - VX/TX</td><td>90</td><td>VTX</td><td>15</td><td>vx_dune2</td><td>9-15</td><td>10/10</td><td class="live">LIVE</td><td class="view">View</td></tr>
<tr><td>#01 - VX/TX</td><td>90</td><td>VTX</td><td>15</td><td>vx_dune2</td><td>9-15</td><td>10/10</td><td class="live">LIVE</td><td class="view">View</td></tr>
<tr><td>#01 - VX/TX</td><td>90</td><td>VTX</td><td>15</td><td>vx_dune2</td><td>9-15</td><td>10/10</td><td class="live">LIVE</td><td class="view">View</td></tr>
<tr><td>#01 - VX/TX</td><td>90</td><td>VTX</td><td>15</td><td>vx_dune2</td><td>9-15</td><td>10/10</td><td class="live">LIVE</td><td class="view">View</td></tr>
<tr><td>#01 - VX/TX</td><td>90</td><td>VTX</td><td>15</td><td>vx_dune2</td><td>9-15</td><td>10/10</td><td class="lobby">LOBBY</td><td class="view">View</td></tr>
<tr><td>#01 - VX/TX</td><td>90</td><td>VTX</td><td>15</td><td>vx_dune2</td><td>9-15</td><td>10/10</td><td class="live">LIVE</td><td class="view">View</td></tr>
<tr><td>#01 - VX/TX</td><td>90</td><td>VTX</td><td>15</td><td>vx_dune2</td><td>9-15</td><td>10/10</td><td class="live">LIVE</td><td class="view">View</td></tr>
<tr><td>#01 - VX/TX</td><td>90</td><td>VTX</td><td>15</td><td>vx_dune2</td><td>9-15</td><td>10/10</td><td class="live">LIVE</td><td class="view">View</td></tr>
<tr><td>#01 - VX/TX</td><td>90</td><td>VTX</td><td>15</td><td>vx_dune2</td><td>9-15</td><td>10/10</td><td class="live">LIVE</td><td class="view">View</td></tr>
<tr><td>#01 - VX/TX</td><td>90</td><td>VTX</td><td>15</td><td>vx_dune2</td><td>9-15</td><td>10/10</td><td class="lobby">LOBBY</td><td class="view">View</td></tr>
<tr><td>#01 - VX/TX</td><td>90</td><td>VTX</td><td>15</td><td>vx_dune2</td><td>9-15</td><td>10/10</td><td class="live">LIVE</td><td class="view">View</td></tr>
<tr><td>#01 - VX/TX</td><td>90</td><td>VTX</td><td>15</td><td>vx_dune2</td><td>9-15</td><td>10/10</td><td class="live">LIVE</td><td class="view">View</td></tr>
<tr><td>#01 - VX/TX</td><td>90</td><td>VTX</td><td>15</td><td>vx_dune2</td><td>9-15</td><td>10/10</td><td class="lobby">LOBBY</td><td class="view">View</td></tr>
<tr><td>#01 - VX/TX</td><td>90</td><td>VTX</td><td>15</td><td>vx_dune2</td><td>9-15</td><td>10/10</td><td class="live">LIVE</td><td class="view">View</td></tr>
<tr><td>#01 - VX/TX</td><td>90</td><td>VTX</td><td>15</td><td>vx_dune2</td><td>9-15</td><td>10/10</td><td class="live">LIVE</td><td class="view">View</td></tr>
    </tbody>
  </table>

  <aside class="abs sidebar">
    <div class="abs side-title">VTX ▸ VX_RUINS2+5pts</div>
    <div class="abs stat-box" style="top:54px;height:139px">
      <div class="head"><span>Online</span><span>Total</span></div>
      <div class="rows">
        <div class="r"><span style="width:125px">Total Users</span>371</div>
        <div class="r"><span style="width:125px">Admin Users</span>2</div>
        <div class="r"><span style="width:125px">Premium Users</span>8</div>
        <div class="r"><span style="width:125px">Normal Users</span>316</div>
        <span class="more">More...</span>
      </div>
    </div>
    <div class="abs stat-box" style="top:206px;height:116px">
      <div class="head"><span style="width:66px">Game</span><span style="width:60px">KPD</span><span>Total</span></div>
      <div class="rows">
        <div class="r"><span style="width:64px">VTX</span><span style="width:61px">0.00~0.80</span>101</div>
        <div class="r"><span style="width:64px">VTX</span><span style="width:61px">0.81~1.39</span>179</div>
        <div class="r"><span style="width:64px">VTX</span><span style="width:61px">1.40 ∞</span>46</div>
      </div>
    </div>
    <form class="abs contact">
      <label>Name:</label><input>
      <label>Email:</label><input>
      <label>Subject:</label><input>
      <label>Message:</label><textarea></textarea>
      <div class="btns"><span>Send</span><span>Clear</span></div>
    </form>
    <div class="abs ad" role="img" aria-label="HostGrid game server provider advertisement"></div>
    <div class="abs follow">Follow Us on
      <div class="icons" role="img" aria-label="Social network links">
        <span style="background:#4fb3e0"></span><span style="background:#3b5998"></span><span style="background:#2a7fb3"></span><span style="background:#e8651c"></span>
      </div>
    </div>
  </aside>
</main>

<div class="abs footer-links">CONTACT US | PRIVACY POLICY | SITEMAP | FEEDS |</div>
<div class="abs copy">© 2009 FragVault 2009</div>
</body>
</html>
```